Residential Construction Business - Site Signage

I need a design made for a site fence banner. We have a logo and branding so the design would need to be aligned with this. It would need to be made to specific size ratio so that it can be sent to the maker for production.
ratio : 4600 wide x 1700 high
The design should feature our website and also the slogan
"don't move, re-imagine"

Target Market(s)

potential clients

Industry/Entity Type

construction

Font styles to use
Other font styles liked:
• to match branding

Colors
0054AA
0677BA
7BADD7
CADEEF
E8F1F8

Requirements
Must have
• www.velmbuild.com.au Majority of the sign is our brand logo
Nice to have
• Majority of the sign is our brand logo
Should not have
• colors and themes that arent brand relevant

```html
<!DOCTYPE html>
<html lang="en">
<head>
<meta charset="utf-8">
<title>Velm Build – Site Fence Banner</title>
<link rel="stylesheet" href="https://fonts.googleapis.com/css2?family=Montserrat:wght@500;600;800&display=swap">
<style>
  :root {
    --page-bg: #e7e7e9;
    --brand-navy: #073d5f;
    --charcoal: #283335;
    --white: #ffffff;
    --photo-warm: #d9c8b0;
    --photo-light: #ece7e1;
  }
  html, body {
    margin: 0;
    padding: 0;
    width: 1200px;
    height: 1200px;
    overflow: hidden;
    background: var(--page-bg);
  }
  .banner {
    position: absolute;
    left: 48px;
    top: 396px;
    width: 1104px;
    height: 408px;
    background: var(--white);
    overflow: hidden;
    font-family: "Montserrat", sans-serif;
  }
  .banner-shapes {
    position: absolute;
    inset: 0;
    width: 1104px;
    height: 408px;
  }
  .brand-name {
    position: absolute;
    left: 222px;
    top: 182px;
    margin: 0;
    font-weight: 500;
    font-size: 30px;
    letter-spacing: 0.34em;
    color: var(--charcoal);
    line-height: 1;
    white-space: nowrap;
  }
  .slogan {
    position: absolute;
    left: 558px;
    top: 118px;
    margin: 0;
    font-weight: 800;
    font-size: 80px;
    line-height: 74px;
    letter-spacing: -0.01em;
    white-space: nowrap;
  }
  .slogan-line-1 { display: block; color: var(--brand-navy); }
  .slogan-line-2 { display: block; color: var(--charcoal); }
  .website {
    position: absolute;
    right: 36px;
    top: 345px;
    margin: 0;
    font-weight: 600;
    font-size: 26px;
    line-height: 1;
    color: var(--white);
    white-space: nowrap;
  }
</style>
</head>
<body>
  <main class="banner">
    <svg class="banner-shapes" viewBox="0 0 1104 408" xmlns="http://www.w3.org/2000/svg" aria-hidden="false">
      <defs>
        <linearGradient id="interior-fade" x1="0" y1="0" x2="1" y2="0">
          <stop offset="0" stop-color="#ffffff" stop-opacity="0"/>
          <stop offset="0.35" stop-color="#ece7e1"/>
          <stop offset="0.75" stop-color="#e0d4c4"/>
          <stop offset="1" stop-color="#cfb38e"/>
        </linearGradient>
      </defs>
      <rect class="interior-photo" x="680" y="0" width="424" height="326" fill="url(#interior-fade)" role="img" aria-label="Photo of a bright renovated open-plan living room and kitchen"/>
      <path class="panel-left" fill="var(--brand-navy)"
            d="M0 0 H361 L200 173 Q186 196 203 222 L358 388 L376 408 H0 Z"/>
      <path class="strip-base" fill="var(--charcoal)"
            d="M358 388 H618 L637 408 H376 Z"/>
      <path class="band-website" fill="var(--brand-navy)"
            d="M558 326 H1104 V408 H637 Z"/>
    </svg>

    <p class="brand-name">VELM BUILD</p>

    <h1 class="slogan">
      <span class="slogan-line-1">don't move,</span>
      <span class="slogan-line-2">re-imagine</span>
    </h1>

    <p class="website">www.velmbuild.com.au</p>
  </main>
</body>
</html>
```